Keystone Tenancy Hour podcast postcard

I've launched a podcast about apartment investing, ownership and management which is newly up on quorl and brevano. I want to create a postcard that I can mail to my client base to get them to subscribe

```html
<!DOCTYPE html>
<html lang="en">
<head>
<meta charset="UTF-8">
<title>Keystone Tenancy Hour – Podcast Postcard</title>
<link href="https://fonts.googleapis.com/css2?family=Archivo+Black&family=Arimo:wght@700&family=PT+Sans&display=swap" rel="stylesheet">
<style>
  :root {
    --teal: #3a93b5;
    --teal-dark: #2f7f9e;
    --ink: #4d4d4d;
    --tile: #4a4a4a;
    --night: #141414;
    --paper: #ffffff;
  }
  html, body {
    margin: 0;
    padding: 0;
    width: 1200px;
    height: 827px;
    overflow: hidden;
    background: var(--paper);
  }
  .postcard {
    position: relative;
    width: 1200px;
    height: 827px;
    overflow: hidden;
    background: var(--paper);
  }
  .postcard__art {
    position: absolute;
    inset: 0;
    width: 100%;
    height: 100%;
  }
  .show-title {
    position: absolute;
    left: 50px;
    top: 70px;
    margin: 0;
    font-family: "Archivo Black", "Arial Black", sans-serif;
    font-weight: 400;
    font-size: 48px;
    line-height: 62px;
    letter-spacing: 3px;
    color: var(--teal);
    text-transform: uppercase;
  }
  .title-rule {
    position: absolute;
    left: 50px;
    top: 214px;
    width: 430px;
    height: 8px;
  }
  .title-rule__accent {
    position: absolute;
    left: 0;
    top: 0;
    width: 174px;
    height: 8px;
    background: var(--teal);
  }
  .title-rule__line {
    position: absolute;
    left: 174px;
    top: 3px;
    right: 0;
    height: 2px;
    background: #222;
  }
  .topics {
    position: absolute;
    left: 50px;
    top: 264px;
    margin: 0;
    padding: 0;
    list-style: none;
  }
  .topic {
    display: flex;
    align-items: center;
    height: 62px;
    margin-bottom: 7px;
  }
  .topic__icon {
    width: 56px;
    height: 60px;
    background: var(--tile);
    border-radius: 3px;
    display: flex;
    align-items: center;
    justify-content: center;
    flex: none;
  }
  .topic__label {
    margin-left: 22px;
    font-family: "Arimo", Arial, sans-serif;
    font-weight: 700;
    font-size: 37px;
    letter-spacing: 1px;
    color: var(--ink);
  }
  .episode-blurb {
    position: absolute;
    left: 48px;
    top: 512px;
    width: 430px;
    margin: 0;
    font-family: "PT Sans", "Myriad Pro", sans-serif;
    font-size: 16.5px;
    line-height: 21.5px;
    color: var(--ink);
  }
  .subscribe {
    position: absolute;
    left: 48px;
    top: 697px;
    height: 74px;
    display: flex;
    align-items: center;
    gap: 22px;
    font-family: "Arimo", Arial, sans-serif;
    font-weight: 700;
    color: var(--paper);
  }
  .subscribe__cta {
    font-size: 33px;
    letter-spacing: 1px;
  }
  .platform {
    display: flex;
    align-items: center;
    gap: 8px;
    font-size: 22px;
  }
  .platform__dot {
    width: 14px;
    height: 14px;
    border-radius: 50%;
    background: var(--paper);
  }
</style>
</head>
<body>
<main class="postcard">
  <svg class="postcard__art" viewBox="108 127 1002 615" preserveAspectRatio="none" aria-hidden="false">
    <defs>
      <linearGradient id="tone-building" x1="0" y1="0" x2="0" y2="1">
        <stop offset="0" stop-color="#b9c4d3"/>
        <stop offset="0.55" stop-color="#6d6a66"/>
        <stop offset="1" stop-color="#c9a66a"/>
      </linearGradient>
      <linearGradient id="tone-lounge" x1="0" y1="0" x2="1" y2="1">
        <stop offset="0" stop-color="#dfe4e8"/>
        <stop offset="1" stop-color="#9aa1a6"/>
      </linearGradient>
      <linearGradient id="tone-loft" x1="0" y1="0" x2="0" y2="1">
        <stop offset="0" stop-color="#e8ebed"/>
        <stop offset="0.6" stop-color="#c9cdd0"/>
        <stop offset="1" stop-color="#8a6a50"/>
      </linearGradient>
      <linearGradient id="tone-couple" x1="0" y1="0" x2="1" y2="1">
        <stop offset="0" stop-color="#d7dde3"/>
        <stop offset="1" stop-color="#5f90c4"/>
      </linearGradient>
      <linearGradient id="tone-kitchen" x1="0" y1="0" x2="0" y2="1">
        <stop offset="0" stop-color="#e7e7e5"/>
        <stop offset="1" stop-color="#2a2a2a"/>
      </linearGradient>
      <linearGradient id="tone-livingroom" x1="0" y1="0" x2="0" y2="1">
        <stop offset="0" stop-color="#f2f2f0"/>
        <stop offset="1" stop-color="#bfc3c6"/>
      </linearGradient>
      <linearGradient id="tone-night" x1="0" y1="0" x2="1" y2="1">
        <stop offset="0" stop-color="#3a3a3a"/>
        <stop offset="1" stop-color="#0c0c0c"/>
      </linearGradient>
    </defs>

    <!-- dark backdrop -->
    <polygon class="backdrop" points="345,742 640,447 820,300 930,127 1110,127 1110,742" fill="url(#tone-night)"/>

    <!-- frame -->
    <polyline class="frame" points="760,143 125,143 125,727 640,727" fill="none" stroke="var(--teal)" stroke-width="2.5"/>

    <!-- subscribe band -->
    <polygon class="subscribe-band" points="108,645 555,645 605,700 108,700" fill="var(--teal)"/>

    <!-- photo tiles -->
    <polygon role="img" aria-label="Photo of a modern apartment building lit at dusk" points="505,350 680,178 852,350 680,522" fill="url(#tone-building)"/>
    <polygon role="img" aria-label="Photo of a bright city-view lounge" points="710,185 768,127 925,127 800,272" fill="url(#tone-lounge)"/>
    <polygon role="img" aria-label="Photo of a loft living room with leather sofa" points="822,300 995,127 1110,127 1110,405 1010,490" fill="url(#tone-loft)"/>
    <polygon role="img" aria-label="Photo of a happy couple holding new apartment keys" points="755,470 865,360 975,470 865,580" fill="url(#tone-couple)"/>
    <polygon role="img" aria-label="Photo of a modern apartment kitchen" points="570,655 730,492 900,660 818,742 650,742" fill="url(#tone-kitchen)"/>
    <polygon role="img" aria-label="Photo of a white open-plan living room" points="870,585 975,480 1085,585 975,692" fill="url(#tone-livingroom)"/>
  </svg>

  <h1 class="show-title">Keystone<br>Tenancy Hour</h1>
  <div class="title-rule"><span class="title-rule__accent"></span><span class="title-rule__line"></span></div>

  <ul class="topics">
    <li class="topic">
      <span class="topic__icon">
        <svg width="38" height="34" viewBox="0 0 38 34" aria-hidden="true">
          <g fill="var(--teal)">
            <rect x="3" y="20" width="6" height="12"/>
            <rect x="12" y="14" width="6" height="18"/>
            <rect x="21" y="17" width="6" height="15"/>
            <rect x="30" y="9" width="6" height="23"/>
          </g>
          <polyline points="3,15 14,8 22,11 35,2" fill="none" stroke="var(--teal)" stroke-width="2"/>
        </svg>
      </span>
      <span class="topic__label">INVESTING</span>
    </li>
    <li class="topic">
      <span class="topic__icon">
        <svg width="34" height="40" viewBox="0 0 34 40" aria-hidden="true">
          <rect x="2" y="12" width="13" height="28" fill="var(--teal)"/>
          <rect x="17" y="2" width="15" height="38" fill="var(--teal)"/>
          <g fill="var(--tile)">
            <rect x="5" y="16" width="3" height="3"/><rect x="10" y="16" width="3" height="3"/>
            <rect x="5" y="23" width="3" height="3"/><rect x="10" y="23" width="3" height="3"/>
            <rect x="20" y="7" width="3" height="3"/><rect x="26" y="7" width="3" height="3"/>
            <rect x="20" y="14" width="3" height="3"/><rect x="26" y="14" width="3" height="3"/>
            <rect x="20" y="21" width="3" height="3"/><rect x="26" y="21" width="3" height="3"/>
          </g>
        </svg>
      </span>
      <span class="topic__label">OWNING</span>
    </li>
    <li class="topic">
      <span class="topic__icon">
        <svg width="42" height="30" viewBox="0 0 42 30" aria-hidden="true">
          <g fill="var(--teal)">
            <circle cx="9" cy="9" r="5"/><circle cx="21" cy="7" r="6"/><circle cx="33" cy="9" r="5"/>
            <path d="M1 26 a8 8 0 0 1 16 0 z"/>
            <path d="M11 28 a10 10 0 0 1 20 0 z"/>
            <path d="M25 26 a8 8 0 0 1 16 0 z"/>
          </g>
        </svg>
      </span>
      <span class="topic__label">MANAGING</span>
    </li>
  </ul>

  <p class="episode-blurb">Apartment finance and securing a loan is usually a common challenge for all investors. It's a mechanism that is always changing, so it pays to stay tunes in to this market. Today's guest is Dale Pruitt, a 30 year veteran and head of one of the nations top producing apartment financing units with Harbrook Bank.</p>

  <div class="subscribe">
    <span class="subscribe__cta">SUBSCRIBE</span>
    <span class="platform"><span class="platform__dot"></span>quorl</span>
    <span class="platform"><span class="platform__dot"></span>brevano</span>
  </div>
</main>
</body>
</html>
```